Plakat-Design für eine Werbeschild für ein Geflügelhof
Zielgruppe
Wir sind ein Geflügelhof, Landhandel, Hofladen, Eier stehen seit über 100 Jahren für Hof Lernstedt, artgerechte Tierhaltung und Artikelvielfalt machen uns bekannt.
Aufgabenstellung
Das Werbeschild wird auf dem Hof aufgestellt und soll den Weg zum Hof zeigen.
- die Maße vom Schild: 1,50m breit x 2,40m hoch
- Grafiken werden als .ai und .pdf benötigt
- Logo ist hochgelagen
- Foto von unserer Vorstellung ist hochgeladen
Das Schild muss 400 m RECHTS drauf gedruckt haben.
Falls es zu breit wäre, könnte das Logo ja vielleicht auch über Hof Lernstedt.
Das ganze wird bei plakwerk auf eine MetaPlanko-Platte in den Druck gegeben.

```html
<!DOCTYPE html>
<html lang="de">
<head>
<meta charset="utf-8">
<title>Hof Lernstedt – Wegweiser</title>
<link rel="stylesheet" href="https://fonts.googleapis.com/css2?family=Dancing+Script:wght@700&family=Open+Sans:wght@700&display=swap">
<style>
  :root {
    --backdrop: #e6e6e6;
    --paper: #ffffff;
    --farm-green: #1e6e34;
    --meadow: #9dc423;
    --meadow-light: #c7df7a;
    --headline-orange: #f08c00;
    --sign-text: #ffffff;
  }
  * { margin: 0; padding: 0; box-sizing: border-box; }
  html, body {
    width: 848px; height: 1200px; overflow: hidden;
    background: var(--backdrop);
  }
  .sign {
    position: absolute; left: 54px; top: 5px;
    width: 740px; height: 1190px;
    background: var(--paper);
    overflow: hidden;
  }
  .brand {
    position: absolute; left: 53px; top: 80px;
    display: flex; align-items: center; gap: 24px;
  }
  .brand-dot {
    width: 112px; height: 112px; border-radius: 50%;
    background: var(--farm-green);
  }
  .brand-name {
    font-family: "Open Sans", sans-serif; font-weight: 700;
    font-size: 58px; color: var(--farm-green); letter-spacing: 0.5px;
  }
  .headline {
    position: absolute; left: 0; width: 100%;
    font-family: "Dancing Script", cursive; font-weight: 700;
    color: var(--headline-orange); text-align: center; line-height: 1;
  }
  .headline-top { top: 250px; font-size: 112px; }
  .headline-main { top: 370px; font-size: 168px; }
  .farm-scene {
    position: absolute; left: 0; top: 600px;
    width: 100%; height: 380px;
    background: linear-gradient(to bottom,
      rgba(255,255,255,0) 0%, #5e9a3a 45%, var(--farm-green) 65%, var(--meadow) 100%);
  }
  .meadow-band {
    position: absolute; left: 0; top: 980px;
    width: 100%; height: 210px;
    background: var(--meadow);
  }
  .direction {
    position: absolute; left: 55px; top: 960px;
    font-family: "Open Sans", sans-serif; font-weight: 700;
    font-size: 70px; color: var(--sign-text); letter-spacing: -0.5px;
  }
  .direction-arrow {
    position: absolute; left: 381px; top: 1066px;
    width: 305px; height: 90px;
  }
</style>
</head>
<body>
  <div class="sign">
    <div class="brand">
      <div class="brand-dot"></div>
      <span class="brand-name">Hof Lernstedt</span>
    </div>

    <div class="headline headline-top">Einkauf auf dem</div>
    <div class="headline headline-main">Bauernhof</div>

    <div class="farm-scene" role="img" aria-label="Silhouetten eines Huhns und einer Ente auf einer Blumenwiese mit Gras und Schmetterlingen"></div>
    <div class="meadow-band"></div>

    <div class="direction">400 Meter rechts</div>
    <svg class="direction-arrow" viewBox="0 0 305 90" aria-hidden="true">
      <g fill="none" stroke="var(--sign-text)" stroke-width="7" stroke-linecap="round" stroke-linejoin="round">
        <line x1="3" y1="45" x2="298" y2="45"/>
        <polyline points="236,4 298,45 236,86"/>
      </g>
    </svg>
  </div>
</body>
</html>
```